M&A Advisory firm needs elegant and powerful letterhead

We need a powerful but elegant letterhead to engage with the international financial industry.

Target Market(s)

New York and International Financial Industry

Industry/Entity Type

Finance

Font styles to use
Other font styles liked:
• Poppins

Requirements
Must have
• 482 W 71st Street 14th Floor New York, NY 10157 O: +1 (212) 555 0147 F: +1 (212) 555 0182

```html
<!DOCTYPE html>
<html lang="en">
<head>
<meta charset="utf-8">
<title>Meridane Letterhead</title>
<link rel="stylesheet" href="https://fonts.googleapis.com/css2?family=Poppins:wght@400;500&display=swap">
<style>
  :root {
    --backdrop: #e4e5e7;
    --paper: #ffffff;
    --brand-blue: #0f5298;
    --contact-blue: #1d5fa6;
    --ink: #2a2a2a;
    --band-grey: #7b7d82;
    --sign-tone: #dfe6f4;
  }
  * { margin: 0; padding: 0; box-sizing: border-box; }
  html, body {
    width: 1200px; height: 900px; overflow: hidden;
    background: var(--backdrop);
    font-family: "Poppins", sans-serif;
  }
  .letterhead {
    position: absolute; left: 305px; top: 33px;
    width: 589px; height: 834px;
    background: var(--paper);
    box-shadow: 0 2px 10px rgba(0,0,0,0.18);
    overflow: hidden;
  }
  .brand {
    position: absolute; left: 42px; top: 38px;
    display: flex; align-items: center; gap: 10px;
  }
  .brand-dot {
    width: 34px; height: 34px; border-radius: 50%;
    background: var(--brand-blue);
  }
  .brand-name {
    font-weight: 400; font-size: 33px; letter-spacing: 0.5px;
    color: var(--brand-blue); line-height: 1;
  }
  .contact {
    position: absolute; left: 428px; top: 27px;
    font-size: 10px; line-height: 14.5px;
    color: var(--contact-blue);
    list-style: none;
  }
  .contact svg { width: 9px; height: 8px; vertical-align: -0.5px; margin-right: 2px; fill: #6d6f73; }
  .body-copy {
    position: absolute; left: 84px; top: 274px; width: 418px;
    font-size: 10.6px; line-height: 13px; color: var(--ink);
    text-align: justify;
  }
  .body-copy p + p { margin-top: 13px; }
  .signature {
    position: absolute; left: 78px; top: 608px;
    width: 148px; height: 34px; border-radius: 4px;
    background: linear-gradient(90deg, var(--sign-tone), #eef2fa);
  }
  .signatory {
    position: absolute; left: 84px; top: 643px;
    font-size: 11px; color: var(--ink);
  }
  .footer-bands {
    position: absolute; left: 0; bottom: 7px;
    width: 589px; height: 30px;
  }
</style>
</head>
<body>
  <main class="letterhead">
    <header>
      <div class="brand">
        <span class="brand-dot"></span>
        <span class="brand-name">MERIDANE</span>
      </div>
      <ul class="contact">
        <li>482 W 71st Street, 14th Floor</li>
        <li>New York, NY 10157</li>
        <li><svg viewBox="0 0 10 8" aria-hidden="true"><path d="M1 3 Q5 0 9 3 L8 4 L6.5 3.3 L6.5 2.5 Q5 2 3.5 2.5 L3.5 3.3 L2 4 Z M2.5 4.5 H7.5 L8.5 8 H1.5 Z"/></svg>+1 (212) 555 0147</li>
        <li><svg viewBox="0 0 10 8" aria-hidden="true"><path d="M2.5 0 H7.5 V2.5 H2.5 Z M0.5 3 H9.5 V7.5 H0.5 Z"/></svg>+1 (212) 555 0182</li>
      </ul>
    </header>

    <section class="body-copy">
      <p>Letterhead samples are a great way of deciding what kind of letterhead you want to design for you and your company. The internet has a ton of great letterhead samples to browse through. Whether you want something simple, with just a couple lines of text of your business information, or something decorative and stunning, with photos and logos on the top and bottom of the page, it will be easy to find what you want, because there are samples online for basically any type of letterhead you could want.</p>
      <p>Any business could easily benefit from browsing through some letterhead samples, if only to get an idea for what kind of letterhead their company might want. Letterheads are just one of the tools that a business professional could use to help increase their customer base, and to really be memorable to everyone they write a letter to. Letterhead is quite an effective tool for marketing and advertising, but because it's such a simple and well known idea, it is often unfairly overlooked. Make sure you don't make that mistake, and make some letterhead samples of your own today.</p>
      <p>Whether you want to get new customers to remember you and become part of your clientele, or you just want to send out friendly reminders to your existing clients, customizing your own letterhead samples can really help you out. Try out some letterhead samples and you will not regret it, and I'm sure you will add a new tool to your business' arsenal of networking, marketing, and advertising tools.</p>
    </section>

    <div class="signature" role="img" aria-label="Handwritten signature of Daniel Harrow"></div>
    <p class="signatory">company director</p>

    <svg class="footer-bands" viewBox="0 0 589 30" aria-hidden="true">
      <path d="M487 0 H589 V30 H0 V21 H474 Z" fill="var(--brand-blue)"/>
      <path d="M0 10 H480 L474 20 H0 Z" fill="var(--band-grey)"/>
    </svg>
  </main>
</body>
</html>
```